Harvest of Kingdoms
preparing the way of the Lord...
Modern
Tom Farrel
412 Co.Rd. 118 Marlow, Pa.17602
tomjane4Faith@postvale.com
www.tf-harvestofkingdoms.com
preaching the gospel of Jesus, and teaching others to do the same.
mission trips
rallies and revivals
camps
this is for business cards and letterhead...

```html
<!DOCTYPE html>
<html lang="en">
<head>
<meta charset="utf-8">
<title>Harvest of Kingdoms — Stationery</title>
<link rel="stylesheet" href="https://fonts.googleapis.com/css2?family=Cinzel:wght@600&family=Lato:ital,wght@0,400;1,400&display=swap">
<style>
  :root{
    --backdrop:#e9e6e1;
    --paper:#ffffff;
    --paper-soft:#f6f6f6;
    --ink:#1b1b1b;
    --band:#141414;
    --accent:#5cc24a;
    --soft:#6d6d6d;
    --rule:#d9d9d9;
  }
  *{box-sizing:border-box;margin:0;padding:0}
  html,body{width:1200px;height:444px;overflow:hidden;background:var(--backdrop)}
  body{position:relative;font-family:"Lato",Arial,sans-serif;color:var(--ink)}

  .piece{position:absolute;background:var(--paper);box-shadow:0 2px 6px rgba(0,0,0,.18);overflow:hidden}
  .piece svg.trim{position:absolute;inset:0;width:100%;height:100%}

  .brand{position:absolute;font-family:"Cinzel",Georgia,serif;font-weight:600;color:var(--ink);line-height:1.05;white-space:nowrap}
  .tagline{position:absolute;font-style:italic;color:var(--soft);white-space:nowrap}
  .contact{position:absolute;color:var(--soft);line-height:1.75;white-space:nowrap}
  .dot{display:inline-block;border-radius:50%;background:var(--accent);vertical-align:middle}

  /* standalone mark */
  .mark{position:absolute;left:20px;top:66px}
  .mark .brand{position:static;font-size:17px}
  .mark .tagline{position:static;display:block;font-size:7px;margin-top:5px}

  /* business cards */
  .card{left:17px;width:180px;height:100px}
  .card-front{top:168px}
  .card-back{top:307px}
  .card .brand{left:12px;top:30px;font-size:11px}
  .card .tagline{left:12px;top:60px;font-size:5px}
  .card .holder{position:absolute;left:92px;top:22px;font-family:"Cinzel",Georgia,serif;font-weight:600;font-size:7px;color:var(--accent)}
  .card .contact{left:92px;top:34px;font-size:4.6px}

  /* letterheads */
  .letterhead{top:29px;width:298px;height:389px}
  .lh-one{left:211px}
  .lh-two{left:528px}
  .letterhead .brand{top:20px;font-size:13px}
  .letterhead .tagline{top:50px;font-size:5px}
  .lh-one .brand,.lh-one .tagline{left:30px}
  .lh-two .brand{left:0;right:0;text-align:center}
  .lh-two .tagline{left:0;right:0;text-align:center}
  .lh-one .contact{left:160px;top:22px;font-size:4.6px}
  .letterhead .footer{position:absolute;left:30px;right:40px;bottom:12px;font-size:4.6px;color:var(--soft);border-top:1px solid var(--rule);padding-top:4px;white-space:nowrap;overflow:hidden}

  /* envelopes */
  .envelope{left:840px;width:336px}
  .env-back{top:29px;height:92px;background:var(--paper-soft)}
  .env-back .brand{left:0;right:0;top:34px;text-align:center;font-size:6px;color:#fff}
  .env-front{top:128px;height:100px}
  .env-front .brand{left:0;right:0;top:46px;text-align:center;font-size:6px}

  /* compliment slip */
  .compliment{left:840px;top:276px;width:336px;height:137px}
  .compliment .brand{left:22px;top:24px;font-size:13px}
  .compliment .tagline{left:22px;top:58px;font-size:5px}
</style>
</head>
<body>

  <div class="mark">
    <div class="brand">Harvest of<br>Kingdoms</div>
    <span class="tagline">preparing the way of the Lord...</span>
  </div>

  <div class="piece card card-front">
    <svg class="trim" viewBox="0 0 180 100" preserveAspectRatio="none" aria-hidden="true">
      <path d="M180 0 L180 100 L164 100 Q178 50 170 0 Z" fill="var(--band)"/>
      <path d="M170 0 Q178 50 164 100" fill="none" stroke="var(--accent)" stroke-width="1.2"/>
    </svg>
    <div class="brand">Harvest of<br>Kingdoms</div>
    <div class="tagline">preparing the way of the Lord...</div>
    <div class="holder">Tom Farrel</div>
    <div class="contact">412 Co.Rd. 118 Marlow, Pa.17602<br>(570) 555-0143<br>tomjane4Faith@postvale.com<br>www.tf-harvestofkingdoms.com</div>
  </div>

  <div class="piece card card-back">
    <svg class="trim" viewBox="0 0 180 100" preserveAspectRatio="none" aria-hidden="true">
      <path d="M180 0 L180 100 L164 100 Q178 50 170 0 Z" fill="var(--band)"/>
      <path d="M170 0 Q178 50 164 100" fill="none" stroke="var(--accent)" stroke-width="1.2"/>
    </svg>
    <div class="brand">Harvest of<br>Kingdoms</div>
    <div class="tagline">preparing the way of the Lord...</div>
    <div class="holder">Tom Farrel</div>
    <div class="contact">412 Co.Rd. 118<br>Marlow, Pa.17602</div>
  </div>

  <div class="piece letterhead lh-one">
    <svg class="trim" viewBox="0 0 298 389" preserveAspectRatio="none" aria-hidden="true">
      <path d="M0 0 L22 0 Q6 30 0 70 Z" fill="var(--band)"/>
      <path d="M22 0 Q6 30 0 70" fill="none" stroke="var(--accent)" stroke-width="1.2"/>
      <path d="M298 389 L298 320 Q292 362 276 389 Z" fill="var(--band)"/>
      <path d="M298 320 Q292 362 276 389" fill="none" stroke="var(--accent)" stroke-width="1.2"/>
    </svg>
    <div class="brand">Harvest of<br>Kingdoms</div>
    <div class="tagline">preparing the way of the Lord...</div>
    <div class="contact">412 Co.Rd. 118 Marlow, Pa.17602<br>(570) 555-0143<br>tomjane4Faith@postvale.com<br>www.tf-harvestofkingdoms.com</div>
    <div class="footer">preaching the gospel of Jesus, and teaching others to do the same.</div>
  </div>

  <div class="piece letterhead lh-two">
    <svg class="trim" viewBox="0 0 298 389" preserveAspectRatio="none" aria-hidden="true">
      <path d="M0 0 L22 0 Q6 30 0 70 Z" fill="var(--band)"/>
      <path d="M22 0 Q6 30 0 70" fill="none" stroke="var(--accent)" stroke-width="1.2"/>
      <path d="M298 389 L298 320 Q292 362 276 389 Z" fill="var(--band)"/>
      <path d="M298 320 Q292 362 276 389" fill="none" stroke="var(--accent)" stroke-width="1.2"/>
    </svg>
    <div class="brand">Harvest of<br>Kingdoms</div>
    <div class="tagline">preparing the way of the Lord...</div>
    <div class="footer">412 Co.Rd. 118 Marlow, Pa.17602 · tomjane4Faith@postvale.com · www.tf-harvestofkingdoms.com</div>
  </div>

  <div class="piece envelope env-back">
    <svg class="trim" viewBox="0 0 336 92" preserveAspectRatio="none" aria-hidden="true">
      <path d="M0 0 L336 0 L336 10 L168 52 L0 10 Z" fill="var(--band)"/>
      <path d="M0 10 L168 52 L336 10" fill="none" stroke="var(--accent)" stroke-width="1.2"/>
      <path d="M0 92 L150 58 M336 92 L186 58" stroke="var(--rule)" stroke-width="1"/>
    </svg>
    <div class="brand"><span class="dot" style="width:5px;height:5px;margin-right:3px"></span>Harvest of Kingdoms</div>
  </div>

  <div class="piece envelope env-front">
    <svg class="trim" viewBox="0 0 336 100" preserveAspectRatio="none" aria-hidden="true">
      <path d="M0 0 L168 40 L336 0" fill="none" stroke="var(--rule)" stroke-width="1"/>
    </svg>
    <div class="brand"><span class="dot" style="width:5px;height:5px;margin-right:3px"></span>Harvest of Kingdoms</div>
  </div>

  <div class="piece compliment">
    <svg class="trim" viewBox="0 0 336 137" preserveAspectRatio="none" aria-hidden="true">
      <path d="M0 0 L18 0 Q6 14 0 32 Z" fill="var(--band)"/>
      <path d="M18 0 Q6 14 0 32" fill="none" stroke="var(--accent)" stroke-width="1.2"/>
      <path d="M336 137 L336 96 Q330 122 312 137 Z" fill="var(--band)"/>
      <path d="M336 96 Q330 122 312 137" fill="none" stroke="var(--accent)" stroke-width="1.2"/>
    </svg>
    <div class="brand">Harvest of<br>Kingdoms</div>
    <div class="tagline">412 Co.Rd. 118 Marlow, Pa.17602</div>
  </div>

</body>
</html>
```